Book cover design for title:

KNOT
Turning Crews into Clans.

Author Norma Vellick

This is my second book the first one is The Hum Shaping a Flourishing and Cooperative Crew Growth Climate ( see cover on www.normavellick.example).

I am after a cover that echoes the title of The Hum, (ie big bold lettering for the word KNOT but not necessarily the images on the front. Although stylised figures are more the style I am after than realist photos. Strong colours and bold statement.

It is about teams that are able to thrive in the complexity of the fast paced and disruptive nature of the world today. 21st century tribes who connect fast to purpose and to each other.

My LinkedIn Norma Vellick and my website give you a flavour of what I do and how I do it.

```html
<!DOCTYPE html>
<html lang="en">
<head>
<meta charset="utf-8">
<title>KNOT – Book Cover Spread</title>
<link href="https://fonts.googleapis.com/css2?family=Montserrat:wght@500;600;700&family=Ubuntu:wght@700&display=swap" rel="stylesheet">
<style>
  :root {
    --navy: #2d2466;
    --navy-deep: #28205e;
    --purple: #8e2a93;
    --white: #ffffff;
    --ink: #1f1960;
    --rule: #e6e4ee;
    --page-bg: #ffffff;
    --photo-a: #8a8f96;
    --photo-b: #3a3a40;
  }
  * { box-sizing: border-box; margin: 0; padding: 0; }
  html, body { width: 910px; height: 1200px; overflow: hidden; background: var(--page-bg); }

  .spread {
    position: absolute;
    left: 12px; top: 295px;
    width: 852px; height: 587px;
    transform: scale(1.04);
    transform-origin: top left;
    display: flex;
    box-shadow: 0 0 0 1px #e8e8ee;
  }

  /* Back cover */
  .back-cover {
    position: relative;
    width: 400px; height: 587px;
    background: var(--white);
  }
  .back-cover__band { position: absolute; left: 0; right: 0; height: 35px; background: var(--navy); }
  .back-cover__band--top { top: 0; }
  .back-cover__band--bottom { bottom: 0; }
  .author-photo {
    position: absolute;
    left: 148px; top: 110px;
    width: 125px; height: 125px;
    border-radius: 50%;
    background: radial-gradient(circle at 45% 40%, var(--photo-a), var(--photo-b));
  }
  .author-name {
    position: absolute; left: 0; right: 0; top: 251px;
    text-align: center;
    font: 600 15px/1 "Montserrat", sans-serif;
    color: var(--ink);
  }
  .author-rule {
    position: absolute; left: 132px; width: 152px; top: 284px;
    border-top: 1px solid var(--rule);
  }
  .author-bio {
    position: absolute; left: 34px; width: 338px; top: 302px;
    font: 500 6.6px/1.45 "Montserrat", sans-serif;
    color: var(--ink);
    text-align: justify;
    text-align-last: center;
  }
  .author-bio p + p { margin-top: 10px; }

  /* Spine */
  .spine {
    position: relative;
    width: 52px; height: 587px;
    background: var(--navy);
    color: var(--white);
  }
  .spine__subtitle, .spine__title {
    position: absolute;
    left: 50%;
    white-space: nowrap;
    transform: translate(-50%, -50%) rotate(-90deg);
  }
  .spine__subtitle { top: 218px; font: 600 16.5px/1 "Montserrat", sans-serif; }
  .spine__title { top: 450px; font: 700 42px/1 "Ubuntu", sans-serif; letter-spacing: 1px; }

  /* Front cover */
  .front-cover {
    position: relative;
    width: 400px; height: 587px;
    background: var(--navy);
    overflow: hidden;
  }
  .front-cover__shapes { position: absolute; inset: 0; width: 400px; height: 587px; }
  .front-cover__author {
    position: absolute; left: 114px; top: 52px;
    font: 600 15px/1 "Montserrat", sans-serif;
    color: var(--white);
    transform: rotate(-17deg);
    transform-origin: left bottom;
  }
  .front-cover__title {
    position: absolute; left: 0; right: 0; top: 230px;
    text-align: center;
    font: 700 88px/1 "Ubuntu", sans-serif;
    color: var(--white);
    letter-spacing: 1px;
  }
  .front-cover__subtitle {
    position: absolute; left: 0; right: 0; top: 350px;
    text-align: center;
    font: 600 17.5px/1 "Montserrat", sans-serif;
    color: var(--white);
  }
</style>
</head>
<body>
  <main class="spread">
    <section class="back-cover">
      <div class="back-cover__band back-cover__band--top"></div>
      <div class="author-photo" role="img" aria-label="Portrait photograph of the author"></div>
      <h2 class="author-name">Norma Vellick</h2>
      <div class="author-rule"></div>
      <div class="author-bio">
        <p>Norma works with leaders and staff teams who want to build real connection at work. For many years she has helped schools and companies turn groups of busy people into crews that trust each other, share purpose and move quickly together. Her talks and workshops are warm, practical and full of energy, and always focused on people.</p>
        <p>In this book she shows how modern crews can thrive when the world around them is fast, complex and full of change. Drawing on stories from classrooms, offices and boardrooms, she sets out simple habits that help people connect to purpose and to each other. Readers will find tools for clear talk, shared goals and steady trust, along with ideas for leading through doubt and disruption. This is a guide for anyone who wants their team to grow into a true clan that lasts.</p>
      </div>
      <div class="back-cover__band back-cover__band--bottom"></div>
    </section>

    <section class="spine">
      <span class="spine__subtitle">Turning Crews into Clans</span>
      <span class="spine__title">KNOT</span>
    </section>

    <section class="front-cover">
      <svg class="front-cover__shapes" viewBox="0 0 400 587" aria-hidden="true">
        <defs>
          <linearGradient id="accentTop" x1="0" y1="0" x2="1" y2="0.3">
            <stop offset="0" stop-color="#2d2466"/>
            <stop offset="0.55" stop-color="#8e2a93"/>
            <stop offset="1" stop-color="#a0309a"/>
          </linearGradient>
          <linearGradient id="accentBottom" x1="0" y1="1" x2="1" y2="0.4">
            <stop offset="0" stop-color="#9a2e98"/>
            <stop offset="0.6" stop-color="#7a2988"/>
            <stop offset="1" stop-color="#2d2466"/>
          </linearGradient>
        </defs>
        <polygon points="0,0 400,0 400,2 120,80 0,22" fill="url(#accentTop)"/>
        <polygon points="0,22 120,80 400,2 400,14 120,95 0,36" fill="#ffffff"/>
        <line x1="205" y1="58" x2="400" y2="6" stroke="#ffffff" stroke-width="0.8"/>
        <polygon points="0,587 280,505 400,574 400,587" fill="url(#accentBottom)"/>
        <polygon points="0,580 280,492 400,561 400,574 280,505 0,587" fill="#ffffff"/>
      </svg>
      <span class="front-cover__author">Norma Vellick</span>
      <h1 class="front-cover__title">KNOT</h1>
      <p class="front-cover__subtitle">Turning Crews into Clans</p>
    </section>
  </main>
</body>
</html>
```